Brenford Automotive business card
Business card design for Brenford Automotive
Project: Brenford Automotive business card
Brenford Automotive business card - Automotive
Creative Brief
Simple
Wade Pelling
482 Kettle Lane Madison, WI 53790
brenautoco@mailnest.example
Hours: Mon-Thurs 7am-6pm
I want a simple road map on the back of the card, with the business location indicated with a star. The map should include Hwy 37, Hwy 21-29, Quarry Bend Rd, Larkfield Loop / Denholm St, Trobek Rd, Kettle Ln, and Corvell Rd.

```html
<!DOCTYPE html>
<html lang="en">
<head>
<meta charset="utf-8">
<title>Brenford Automotive business card</title>
<link rel="stylesheet" href="https://fonts.googleapis.com/css2?family=Arimo:wght@400;700&display=swap">
<style>
  :root {
    --backdrop: #3b3e43;
    --card: #ffffff;
    --ink: #3d3f44;
    --brand: #24336b;
    --band: #3a3a3c;
    --blue-light: #3fa9e0;
    --blue-dark: #1d5ea8;
    --on-blue: #ffffff;
  }
  html, body {
    margin: 0;
    width: 1200px;
    height: 751px;
    overflow: hidden;
    background: var(--backdrop);
    font-family: "Arimo", Arial, sans-serif;
  }
  .card {
    position: absolute;
    left: 100px;
    top: 83px;
    width: 1000px;
    height: 585px;
    background: var(--card);
    border-radius: 34px;
    overflow: hidden;
  }
  .card-waves {
    position: absolute;
    inset: 0;
    width: 100%;
    height: 100%;
  }
  .brand {
    position: absolute;
    left: 70px;
    top: 180px;
    display: flex;
    align-items: center;
    gap: 14px;
    color: var(--brand);
    font-weight: 700;
    font-size: 40px;
    letter-spacing: 0.5px;
  }
  .brand-dot {
    width: 22px;
    height: 22px;
    border-radius: 50%;
    background: var(--brand);
  }
  .holder-name {
    position: absolute;
    left: 620px;
    top: 66px;
    margin: 0;
    color: var(--ink);
    font-weight: 400;
    font-size: 34px;
    letter-spacing: 1px;
    text-transform: uppercase;
  }
  .contact {
    position: absolute;
    left: 620px;
    top: 352px;
    color: var(--on-blue);
    font-size: 16px;
    line-height: 26px;
    text-transform: uppercase;
    letter-spacing: 0.3px;
  }
  .contact p { margin: 0; }
  .contact .gap { margin-top: 26px; }
</style>
</head>
<body>
  <div class="card">
    <svg class="card-waves" viewBox="0 0 1000 585" preserveAspectRatio="none" aria-hidden="true">
      <defs>
        <linearGradient id="blueFill" x1="0" y1="0" x2="1" y2="0">
          <stop offset="0" stop-color="var(--blue-light)"/>
          <stop offset="1" stop-color="var(--blue-dark)"/>
        </linearGradient>
      </defs>
      <path class="band" fill="var(--band)" d="M0,470 C250,330 600,220 1000,175 L1000,200 C640,240 320,340 95,585 L0,585 Z"/>
      <path class="blue-field" fill="url(#blueFill)" d="M95,585 C320,340 640,240 1000,200 L1000,585 Z"/>
    </svg>

    <div class="brand"><span class="brand-dot"></span>Brenford Automotive</div>

    <h1 class="holder-name">Wade Pelling</h1>

    <div class="contact">
      <p>482 Kettle Lane</p>
      <p>Madison, WI 53790</p>
      <p class="gap">P : (608) 555-0142</p>
      <p class="gap">E : brenautoco@mailnest.example</p>
    </div>
  </div>
</body>
</html>
```